Vortique Energy Business Card Design

website: www.vortiqueenergy.example
Project: Business Card Design for Vortique Energy
Name: Derek Holloway
Title: Founder / Operations Strategist
Visual Identity & Logo:
Logo File: VRT-Logo-FullGradient-Final.png (Attached).
Color Palette: The brand relies on a distinctive Cyan (Blue) to Lime Green gradient.
Background Preference: We want a Dark Mode aesthetic (Deep Matte Black, Charcoal, or Dark Slate) to make the neon gradient of the logo pop. This feels more "tech/industrial" than a standard white card.
Design Aesthetic (The "Ops" Vibe):
Concept: "Grid & Infrastructure." We are a solar rental company, focusing on logistics and access.
Typography: White, bold sans-serif text for contact info. High contrast against the dark background.
Accents: Use the Cyan or Lime Green from the logo for thin divider lines or edge painting.
Avoid: No orange/gold (clashes with logo). No cartoon leaves.
Layout Requirements:
Front: Large, centered logo. Maybe a subtle UV gloss spot varnish over the logo icon.
Back: Name, Title, Contact Info.
Texture: Matte finish cardstock with gloss elements.
sample mock up of information on card: https://brimtolcorp-my.filedock.example/:i:/g/personal/derek_holloway_vortiqueenergy_com/AbCdEfGhIjKlMnOpQrStUvWxYz0123456789AbCdEfGh?e=X1Y2Z3
Logo: https://brimtolcorp.filedock.example/:i:/s/VortiqueEnergy/ZyXwVuTsRqPoNmLkJiHgFeDcBa9876543210ZyXwVuTs?e=Q4R5S6

```html
<!DOCTYPE html>
<html lang="en">
<head>
<meta charset="UTF-8">
<title>Vortique Energy Business Card</title>
<link href="https://fonts.googleapis.com/css2?family=Montserrat:ital,wght@0,400;0,500;0,700;0,800;1,500&display=swap" rel="stylesheet">
<style>
  :root {
    --stage: #c9c9c9;
    --card: #1d1d1e;
    --card-edge: #151515;
    --gloss: rgba(255,255,255,0.05);
    --cyan: #1ba6dc;
    --lime: #a6d13a;
    --white: #f2f2f2;
  }
  * { box-sizing: border-box; margin: 0; padding: 0; }
  html, body { width: 1200px; height: 802px; overflow: hidden; }
  body {
    background: linear-gradient(180deg, #d4d4d4 0%, var(--stage) 55%, #b9b9b9 100%);
    font-family: "Montserrat", sans-serif;
    color: var(--white);
    position: relative;
  }
  .card {
    position: absolute;
    top: 241px;
    width: 560px;
    height: 320px;
    background: var(--card);
    border-radius: 22px;
    overflow: hidden;
    box-shadow: 0 18px 40px rgba(0,0,0,0.35);
  }
  .card::after {
    content: "";
    position: absolute;
    left: 0; right: 0; bottom: 0;
    height: 4px;
    background: linear-gradient(90deg, var(--cyan), var(--lime));
  }
  .card--contact { left: 30px; }
  .card--brand { left: 610px; }
  .gloss-panel {
    position: absolute;
    background: var(--gloss);
    border-radius: 14px;
  }
  .brand-lockup {
    display: flex;
    align-items: center;
    gap: 10px;
    color: var(--cyan);
    font-weight: 500;
  }
  .brand-mark {
    background: var(--cyan);
    border-radius: 3px;
  }
  .card--contact .brand-lockup {
    position: absolute; left: 30px; top: 34px;
    font-size: 26px;
  }
  .card--contact .brand-mark { width: 22px; height: 22px; }
  .edge-tab {
    position: absolute; right: 0; top: 30px;
    width: 8px; height: 22px;
    background: linear-gradient(180deg, var(--cyan), var(--lime));
  }
  .person {
    position: absolute; right: 24px; top: 32px;
    text-align: right;
  }
  .person__name {
    font-weight: 800; font-size: 16px; letter-spacing: 0.5px;
    color: var(--lime);
  }
  .person__title { font-size: 11px; margin-top: 4px; }
  .address {
    position: absolute; left: 30px; top: 170px;
    font-size: 11.5px; line-height: 1.5;
  }
  .contacts {
    position: absolute; left: 30px; top: 222px;
    list-style: none;
    font-size: 12.5px; line-height: 1.75;
  }
  .contacts li { display: flex; align-items: center; gap: 8px; }
  .contacts svg { width: 12px; height: 12px; flex: none; }
  .card--brand .brand-lockup {
    position: absolute; left: 0; right: 0; top: 104px;
    justify-content: center;
    font-size: 44px;
  }
  .card--brand .brand-mark { width: 38px; height: 38px; }
  .tagline {
    position: absolute; left: 0; right: 0; top: 172px;
    text-align: center;
    font-style: italic; font-weight: 500; font-size: 13px;
    letter-spacing: 0.6px;
  }
  .promise {
    position: absolute; left: 0; right: 0; bottom: 34px;
    text-align: center;
    font-size: 12.5px; letter-spacing: 0.4px;
  }
</style>
</head>
<body>

<section class="card card--contact">
  <div class="gloss-panel" style="left:380px; top:150px; width:150px; height:60px;"></div>
  <div class="gloss-panel" style="left:440px; top:220px; width:90px; height:70px;"></div>
  <div class="brand-lockup"><span class="brand-mark"></span>Vortique Energy</div>
  <div class="edge-tab"></div>
  <div class="person">
    <p class="person__name">DEREK HOLLOWAY</p>
    <p class="person__title">Founder / Operations Strategist</p>
  </div>
  <p class="address">Vortique Energy, LLC 4120 Brightwater Loop<br>Marlow, FL 32990</p>
  <ul class="contacts">
    <li>
      <svg viewBox="0 0 12 12"><path fill="#a6d13a" d="M2.5 1l2 2-1 1.5c.7 1.5 1.8 2.6 3.3 3.3L8.3 6.8l2 2-1.3 1.8C5 10.3 1.7 7 1.4 2.3z"/></svg>
      555.014.2276
    </li>
    <li>
      <svg viewBox="0 0 12 12"><rect x="1" y="2.5" width="10" height="7" fill="#a6d13a"/><path d="M1 2.5l5 4 5-4" stroke="#1d1d1e" fill="none"/></svg>
      info@vortiqueenergy.example
    </li>
    <li>
      <svg viewBox="0 0 12 12"><circle cx="6" cy="6" r="5" fill="none" stroke="#a6d13a" stroke-width="1.3"/><path d="M1 6h10M6 1c-2.5 3-2.5 7 0 10M6 1c2.5 3 2.5 7 0 10" stroke="#a6d13a" fill="none" stroke-width="0.9"/></svg>
      www.vortiqueenergy.example
    </li>
  </ul>
</section>

<section class="card card--brand">
  <div class="gloss-panel" style="left:300px; top:-20px; width:300px; height:200px; transform:rotate(-8deg);"></div>
  <div class="gloss-panel" style="left:-40px; top:220px; width:260px; height:140px; transform:rotate(-8deg);"></div>
  <div class="brand-lockup"><span class="brand-mark"></span>Vortique Energy</div>
  <p class="tagline">Rent Solar. Generate Power. Save Smarter</p>
  <p class="promise">No debt, no liens, no maintenance, just savings.</p>
</section>

</body>
</html>
```